We require a banner design for a 53' x 10' trailer for a future development to be displayed on the side of the highway. The development name is 712 35 Commerce Park, logo is attached. This is an industrial future development. Please also include the RLW Group logo and MERO Development logos as well.

Industry/Entity Type

Real Estate / Construction / Developer / Industrial Future Development

Requirements
Must have
• Logos provided

```html
<!DOCTYPE html>
<html lang="en">
<head>
<meta charset="utf-8">
<title>712 35 Commerce Park – Trailer Banner</title>
<link rel="stylesheet" href="https://fonts.googleapis.com/css2?family=Montserrat:wght@400;500;700;800&display=swap">
<style>
  :root {
    --stage: #5e5d5e;
    --paper: #ffffff;
    --ink: #1e1c1d;
    --signal-red: #e8282f;
    --accent-teal: #1a9bd0;
  }
  html, body {
    margin: 0;
    padding: 0;
    width: 1200px;
    height: 1021px;
    overflow: hidden;
    background: var(--stage);
    font-family: "Montserrat", sans-serif;
  }
  .banner {
    position: absolute;
    left: 34px;
    top: 402px;
    width: 1132px;
    height: 216px;
    background: var(--paper);
    box-shadow: 0 12px 40px rgba(0,0,0,0.45);
  }
  .logo-row {
    position: absolute;
    left: 0;
    top: 0;
    width: 100%;
    height: 159px;
    display: flex;
    align-items: center;
    justify-content: space-between;
    padding: 0 40px 0 52px;
    box-sizing: border-box;
  }
  .partner {
    display: flex;
    align-items: center;
    gap: 14px;
    color: var(--ink);
    font-weight: 700;
    line-height: 1.05;
    white-space: nowrap;
  }
  .partner-mark { flex: none; }
  .partner--park .partner-name { font-size: 40px; }
  .partner--group .partner-name { font-size: 50px; letter-spacing: 1px; }
  .partner--dev .partner-name { font-size: 40px; letter-spacing: 4px; }
  .partner-name small {
    display: block;
    font-size: 14px;
    font-weight: 500;
    letter-spacing: 2.5px;
    margin-top: 6px;
  }
  .mark-square {
    width: 40px; height: 40px;
    background: var(--ink);
  }
  .mark-circle {
    width: 46px; height: 46px;
    border-radius: 50%;
    background: var(--signal-red);
  }
  .mark-square--teal { background: var(--accent-teal); }
  .info-band {
    position: absolute;
    left: 0;
    bottom: 0;
    width: 100%;
    height: 57px;
  }
  .info-band svg.band-shapes { position: absolute; inset: 0; }
  .tagline {
    position: absolute;
    left: 14px;
    top: 0;
    height: 57px;
    line-height: 57px;
    color: var(--paper);
    font-weight: 800;
    font-size: 33px;
    letter-spacing: 0.2px;
    margin: 0;
    white-space: nowrap;
  }
  .contact {
    position: absolute;
    left: 610px;
    right: 24px;
    top: 0;
    height: 57px;
    display: flex;
    align-items: center;
    gap: 8px;
    color: var(--paper);
    font-weight: 700;
    white-space: nowrap;
  }
  .contact > * { flex: none; }
  .contact-phone { font-size: 29px; margin-right: 10px; }
  .contact-web { font-size: 27px; }
</style>
</head>
<body>
  <section class="banner" aria-label="712 35 Commerce Park trailer banner">
    <div class="logo-row">
      <div class="partner partner--park">
        <span class="partner-mark mark-square"></span>
        <span class="partner-name">712 35<small>COMMERCE PARK</small></span>
      </div>
      <div class="partner partner--group">
        <span class="partner-mark mark-circle"></span>
        <span class="partner-name">RLW Group</span>
      </div>
      <div class="partner partner--dev">
        <span class="partner-mark mark-square mark-square--teal"></span>
        <span class="partner-name">MERO<small>DEVELOPMENT</small></span>
      </div>
    </div>

    <div class="info-band">
      <svg class="band-shapes" width="1132" height="57" viewBox="0 0 1132 57" aria-hidden="true">
        <polygon points="0,0 572,0 603,57 0,57" fill="var(--signal-red)"/>
        <polygon points="576,0 1132,0 1132,57 607,57" fill="var(--paper)"/>
        <polygon points="588,0 1132,0 1132,57 619,57" fill="var(--ink)"/>
      </svg>
      <p class="tagline">INDUSTRIAL BUSINESS PARK.</p>
      <div class="contact">
        <svg class="icon-phone" width="20" height="20" viewBox="0 0 24 24" aria-hidden="true">
          <path d="M6.6 10.8a15 15 0 0 0 6.6 6.6l2.2-2.2a1 1 0 0 1 1-.25 11.4 11.4 0 0 0 3.6.6 1 1 0 0 1 1 1V20a1 1 0 0 1-1 1A17 17 0 0 1 3 4a1 1 0 0 1 1-1h3.5a1 1 0 0 1 1 1c0 1.25.2 2.45.6 3.6a1 1 0 0 1-.25 1z" fill="var(--signal-red)"/>
        </svg>
        <span class="contact-phone">555.210.4871</span>
        <svg class="icon-globe" width="22" height="22" viewBox="0 0 24 24" aria-hidden="true" fill="none" stroke="var(--signal-red)" stroke-width="1.6">
          <circle cx="12" cy="12" r="10"/>
          <ellipse cx="12" cy="12" rx="4.5" ry="10"/>
          <line x1="2" y1="12" x2="22" y2="12"/>
          <line x1="4" y1="7" x2="20" y2="7"/>
          <line x1="4" y1="17" x2="20" y2="17"/>
        </svg>
        <span class="contact-web">parksite712.com</span>
      </div>
    </div>
  </section>
</body>
</html>
```